Bref créative
BrightHollow Capital Partners
......putting entrepreneurs and investors together
Professional
Marcus Pellow
418 Weldon Avenue
Suite 340
Media, PA 19087
brighthollowcap@mailvista.net
I have selected the black & red color scheme on the logo.
Angel Investors/Angel Funds
Seed/Start-up Investment
Private Equity Funds
Venture Capital Funding
Merchant Funding
Receivable/Purchase Order Funding

```html
<!DOCTYPE html>
<html lang="en">
<head>
<meta charset="utf-8">
<title>BrightHollow Capital Partners – Business Card</title>
<link rel="stylesheet" href="https://fonts.googleapis.com/css2?family=Source+Sans+3:wght@400;600&display=swap">
<style>
  :root {
    --backdrop: #e9e6e1;
    --card: #ffffff;
    --ink: #231f20;
    --text: #2b2b2b;
    --red: #e3232b;
    --rule: #9a9a9a;
  }
  * { margin: 0; padding: 0; box-sizing: border-box; }
  html, body {
    width: 1200px;
    height: 778px;
    overflow: hidden;
    background: var(--backdrop);
    font-family: "Source Sans 3", "Helvetica Neue", Arial, sans-serif;
  }
  .business-card {
    position: absolute;
    left: 40px;
    top: 63px;
    width: 1120px;
    height: 652px;
    background: var(--card);
    border-radius: 40px;
    overflow: hidden;
    box-shadow: 0 4px 14px rgba(0,0,0,0.18);
  }
  .brand {
    position: absolute;
    left: 0;
    width: 1090px;
    top: 86px;
    text-align: center;
    color: var(--ink);
    font-weight: 600;
  }
  .brand-name {
    display: block;
    font-size: 84px;
    line-height: 1;
    letter-spacing: 2px;
  }
  .brand-sub {
    display: block;
    margin-top: 14px;
    font-size: 34px;
    line-height: 1;
    letter-spacing: 17px;
  }
  .holder {
    position: absolute;
    right: 541px;
    top: 316px;
    text-align: right;
    color: var(--text);
  }
  .holder-name {
    color: var(--red);
    font-size: 38px;
    line-height: 1;
    margin-bottom: 22px;
  }
  .holder-address {
    font-style: normal;
    font-size: 31px;
    line-height: 51px;
  }
  .divider {
    position: absolute;
    left: 597px;
    top: 315px;
    width: 2px;
    height: 163px;
    background: var(--rule);
  }
  .contact-list {
    position: absolute;
    left: 612px;
    top: 332px;
    list-style: none;
    color: var(--text);
    font-size: 29px;
    line-height: 1;
  }
  .contact-list li {
    display: flex;
    align-items: center;
    height: 45px;
  }
  .contact-icon {
    width: 22px;
    height: 24px;
    margin-right: 12px;
    fill: var(--red);
    flex: none;
  }
  .swoosh {
    position: absolute;
    left: 0;
    bottom: 0;
    width: 1120px;
    height: 652px;
  }
</style>
</head>
<body>
  <main class="business-card">
    <svg class="swoosh" viewBox="0 0 1120 652" aria-hidden="true">
      <path d="M0 568 C 320 650, 640 640, 1120 505 L1120 652 L0 652 Z" fill="var(--red)"/>
      <path d="M0 520 C 300 610, 640 610, 1120 462" fill="none" stroke="var(--ink)" stroke-width="9"/>
    </svg>

    <header class="brand">
      <span class="brand-name">BRIGHTHOLLOW</span>
      <span class="brand-sub">CAPITAL PARTNERS</span>
    </header>

    <section class="holder">
      <p class="holder-name">Marcus Pellow</p>
      <address class="holder-address">418 Weldon Avenue, Suite 340<br>Media, PA 19087</address>
    </section>

    <div class="divider"></div>

    <ul class="contact-list">
      <li>
        <svg class="contact-icon" viewBox="0 0 22 24" aria-hidden="true">
          <rect x="5" y="1" width="12" height="22" rx="2"/>
          <rect x="7.5" y="4" width="7" height="11" fill="#fff"/>
          <circle cx="11" cy="19" r="1.5" fill="#fff"/>
        </svg>
        610-555-0148
      </li>
      <li>
        <svg class="contact-icon" viewBox="0 0 22 24" aria-hidden="true">
          <path d="M2 6 Q11 0 20 6 L20 9 L15 9 L15 7 Q11 5 7 7 L7 9 L2 9 Z"/>
          <rect x="3" y="11" width="16" height="11" rx="2"/>
          <circle cx="11" cy="16.5" r="2.5" fill="#fff"/>
        </svg>
        610-555-0192
      </li>
      <li>
        <svg class="contact-icon" viewBox="0 0 22 24" aria-hidden="true">
          <rect x="1" y="6" width="20" height="13" rx="1"/>
          <path d="M2 7 L11 14 L20 7" fill="none" stroke="#fff" stroke-width="1.8"/>
        </svg>
        brighthollowcap@mailvista.net
      </li>
    </ul>
  </main>
</body>
</html>
```